Need a stunning looking Business Card Design for my Telecom Business, Wow FACTOR!

I deal with high level IT Directors , and Contractors.
I need to impress them with a sleek , professional and unique business card.
Im thinking options as far as rounded edges, plastic , or even metal card or die cut on a corner.
Whatever looks better and leave an unforgettable first impression.
im looking for the wow factor.
Front should have the basics info (attached on the picture of current business card)
i would like to add picture of myself somewhere
Back side
should have logo and maybe some pictures or past projects, you can download from my website ( www.lumvexholdings.com)

```html
<!DOCTYPE html>
<html lang="en">
<head>
<meta charset="utf-8">
<title>Lumvex Holdings — Business Card</title>
<link rel="stylesheet" href="https://fonts.googleapis.com/css2?family=Montserrat:wght@400;500;700&display=swap">
<style>
  :root {
    --backdrop: #b4b4b4;
    --card-white: #ffffff;
    --brand-blue: #0b5285;
    --navy: #123a64;
    --sky: #2f9fd8;
    --ink: #1e1e1e;
    --rule: #1b5a8c;
    --photo-mid: #9a989a;
    --photo-light: #cfcac6;
  }
  * { box-sizing: border-box; margin: 0; padding: 0; }
  html, body {
    width: 900px; height: 1200px; overflow: hidden;
    background: var(--backdrop);
    font-family: "Montserrat", Arial, sans-serif;
  }
  .canvas { position: relative; width: 900px; height: 1200px; }
  .card {
    position: absolute; left: 80px; width: 742px; height: 438px;
    border-radius: 32px; overflow: hidden;
  }
  .card--front { top: 130px; background: var(--card-white); }
  .card--back { top: 640px; background: var(--brand-blue); }

  .brand {
    position: absolute; left: 36px; top: 52px;
    display: flex; align-items: center; gap: 14px;
  }
  .brand__dot { width: 40px; height: 40px; border-radius: 50%; background: var(--navy); }
  .brand__name { font-weight: 500; font-size: 30px; letter-spacing: 1px; color: var(--ink); }

  .portrait {
    position: absolute; left: 434px; top: 36px; width: 298px; height: 294px;
    border-radius: 140px 140px 0 0;
    background:
      radial-gradient(ellipse 46% 40% at 55% 36%, var(--photo-light) 0%, rgba(207,202,198,0) 100%),
      linear-gradient(180deg, rgba(154,152,154,0) 0%, rgba(154,152,154,0.55) 45%, var(--photo-mid) 100%);
  }

  .person { position: absolute; left: 34px; top: 272px; }
  .person__name { font-size: 27px; font-weight: 500; color: var(--brand-blue); letter-spacing: 0.5px; }
  .person__name strong { font-weight: 700; }
  .person__role { font-size: 16px; color: var(--ink); margin-top: 1px; }

  .divider {
    position: absolute; left: 34px; top: 328px; width: 698px; height: 2px; background: var(--rule);
  }

  .contacts { position: absolute; left: 34px; top: 342px; list-style: none; }
  .contacts li {
    display: flex; align-items: center; gap: 14px;
    font-size: 16px; color: var(--ink); height: 23.5px;
  }
  .contacts svg { width: 18px; height: 18px; fill: var(--navy); flex: none; }

  .offices {
    position: absolute; left: 482px; top: 346px;
    font-size: 15.5px; line-height: 21px; color: var(--ink);
  }
  .offices p + p { margin-top: 4px; }

  .back-brand {
    position: absolute; left: 0; right: 0; top: 96px;
    display: flex; flex-direction: column; align-items: center; gap: 34px;
  }
  .back-brand__dot {
    width: 120px; height: 120px; border-radius: 50%;
    background: radial-gradient(circle at 40% 35%, #5cc0ee 0%, var(--sky) 60%, #1f78b4 100%);
  }
  .back-brand__name { font-weight: 500; font-size: 44px; letter-spacing: 2px; color: #ffffff; }
</style>
</head>
<body>
<main class="canvas">
  <section class="card card--front">
    <div class="brand">
      <span class="brand__dot"></span>
      <span class="brand__name">LUMVEX HOLDINGS</span>
    </div>

    <div class="portrait" role="img" aria-label="Portrait photo of Ray Tanaka in a grey shirt"></div>

    <div class="person">
      <h1 class="person__name"><strong>RAY</strong> TANAKA</h1>
      <p class="person__role">Operation Manager</p>
    </div>

    <div class="divider"></div>

    <ul class="contacts">
      <li>
        <svg viewBox="0 0 24 24" aria-hidden="true"><path d="M6.6 10.8a15.1 15.1 0 0 0 6.6 6.6l2.2-2.2c.3-.3.7-.4 1-.2 1.1.4 2.3.6 3.6.6.6 0 1 .4 1 1V20c0 .6-.4 1-1 1A17 17 0 0 1 3 4c0-.6.4-1 1-1h3.5c.6 0 1 .4 1 1 0 1.3.2 2.5.6 3.6.1.3 0 .7-.2 1z"/></svg>
        <span>(954) 555-0137</span>
      </li>
      <li>
        <svg viewBox="0 0 24 24" aria-hidden="true"><path d="M3 5h18a1 1 0 0 1 1 1v1l-10 6L2 7V6a1 1 0 0 1 1-1zm-1 4.3 10 6 10-6V18a1 1 0 0 1-1 1H3a1 1 0 0 1-1-1z"/></svg>
        <span>www.lumvexholdings.com</span>
      </li>
      <li>
        <svg viewBox="0 0 24 24" aria-hidden="true"><circle cx="12" cy="12" r="9"/><path d="M7 8c2 0 3 1 3 3s-2 2-2 4M15 5c0 2 2 2 2 4s-2 2-3 4 1 3 2 4" stroke="#fff" stroke-width="1.6" fill="none"/></svg>
        <span>info@lumvexholdings.com</span>
      </li>
    </ul>

    <div class="offices">
      <p>Offices in Miami, Browards<br>&amp; Palm Beach</p>
      <p>State License #ES40917326</p>
    </div>
  </section>

  <section class="card card--back">
    <div class="back-brand">
      <span class="back-brand__dot"></span>
      <span class="back-brand__name">LUMVEX HOLDINGS</span>
    </div>
  </section>
</main>
</body>
</html>
```